Bref créative
Bath/Spa Product Label
Vesta Reef
Thanks to you expert graphic artists we have been happy with the logo designed last summer and would like to see what you wizards can do to with a product label.
We have attached the current logo and would love to see what you can do with creating a product label that will fit several types of labels.
1. We need a vertical orientation of the label to be scalable so that we can use it on 16 oz or 8 ounce bottles.
2. We need a horizontal orientation that is also scalable for 8 ounce or 4 ounce jars.
You can place the uploaded logo anywhere on the labels but we need blank space to fill in the product name, net weight, instructions and ingredients.
Feel free to apply generic text for the net weight, instructions and ingredients. We manufacture shampoos, conditioners, body washes, shower gels, body scrubs, foot scrubs, sugar scrubs, etc.
We have attached two sample MS Word documents with the ugly and boring labels we use now. Use these as inspiration to move us to the next level. Go ahead add color, fonts, additional graphics - whatever you see fit. In the past, we have treated our designers fairly and cordially. You can expect the same treatment for this contest.
Personal Care
Over 95% of our customer base is women. But keep in mind that men also use shower gels - so no teddy bears on the product label please.Our clients are used to high quality product, not over hyped claims or garish designs.
As stated above we need the label in at least two orientations. It must also be scalable so that we can use it on different size labels. If you can design a third label in square dimensions that would be a big bonus.
Current jar label - for example DO NOT REPLICATE.
Sample shampoo/body wash label applied vertically to 16 ounce or 8 ounce bottles. FOR EXAMPLE ONLY DO NOT REPLICATE
Current logo - DO NOT DISTRIBUTE - COPYRIGHT VESTA REEF.

```html
<!DOCTYPE html>
<html lang="en">
<head>
<meta charset="utf-8">
<title>Vesta Reef – Sugar Scrub Jar Label</title>
<link rel="stylesheet" href="https://fonts.googleapis.com/css2?family=Cinzel:wght@400&family=Arimo:wght@400;700&display=swap">
<style>
  :root {
    --stage: #6e6e6e;
    --stage-light: #9a9a9a;
    --label-dark: #141414;
    --label-mid: #2e2e2e;
    --panel: #ffffff;
    --gold: #c8963e;
    --bronze: #7a5224;
    --brand-blue: #4a6f8f;
    --ink: #1f2a3a;
    --label-text: #f2f2f2;
  }
  * { box-sizing: border-box; margin: 0; padding: 0; }
  html, body { width: 1200px; height: 850px; overflow: hidden; }
  body {
    background: radial-gradient(ellipse at 50% 35%, var(--stage-light), var(--stage) 75%);
    font-family: "Arimo", Arial, sans-serif;
  }
  .jar-label {
    position: absolute;
    left: 96px; top: 269px;
    width: 1008px; height: 312px;
    background: linear-gradient(180deg, var(--label-mid), var(--label-dark) 45%, var(--label-mid));
    overflow: hidden;
    box-shadow: 0 6px 18px rgba(0,0,0,.35);
  }
  .flourish {
    position: absolute;
    background: radial-gradient(ellipse at center, rgba(150,150,150,.22), rgba(150,150,150,0) 70%);
  }
  .flourish--left { left: 60px; top: 150px; width: 300px; height: 160px; }
  .flourish--right { left: 650px; top: 160px; width: 300px; height: 150px; }
  .center-panel { position: absolute; inset: 0; }
  .product-copy {
    position: absolute;
    color: var(--label-text);
    font-size: 13.5px;
    line-height: 1.32;
    text-align: justify;
  }
  .product-copy--intro { left: 30px; top: 30px; width: 240px; }
  .product-copy--facts { left: 756px; top: 30px; width: 228px; }
  .product-copy p + p { margin-top: 14px; }
  .product-copy strong { font-weight: 700; }
  .brand {
    position: absolute;
    left: 384px; top: 0; width: 240px;
    text-align: center;
  }
  .brand-dot {
    width: 46px; height: 46px;
    margin: 34px auto 0;
    border-radius: 50%;
    background: var(--gold);
  }
  .brand-name {
    margin-top: 14px;
    font-family: "Cinzel", Georgia, serif;
    font-size: 33px;
    letter-spacing: 1px;
    color: var(--brand-blue);
    white-space: nowrap;
    margin-left: -20px; margin-right: -20px;
  }
  .product-name {
    margin: 34px -22px 0;
    font-size: 15px;
    line-height: 1.35;
    color: var(--ink);
  }
</style>
</head>
<body>
  <section class="jar-label">
    <div class="flourish flourish--left" role="img" aria-label="Faint silver scroll flourishes on the dark band"></div>
    <div class="flourish flourish--right" role="img" aria-label="Faint silver scroll flourishes on the dark band"></div>

    <svg class="center-panel" viewBox="0 0 1008 312" width="1008" height="312" aria-hidden="true">
      <path d="M372 0 Q318 156 372 312 L636 312 Q690 156 636 0 Z" fill="var(--bronze)"/>
      <path d="M382 0 Q330 156 382 312 L626 312 Q678 156 626 0 Z" fill="var(--gold)"/>
      <path d="M388 0 Q338 156 388 312 L620 312 Q670 156 620 0 Z" fill="var(--panel)"/>
    </svg>

    <div class="product-copy product-copy--intro">
      <p>A unique blend of safflower oil, sugar and Jojoba beads, to exfoliate and bring a lovely glow to your skin. Scented with invigorating Lavender Mint.</p>
    </div>

    <div class="brand">
      <div class="brand-dot"></div>
      <h1 class="brand-name">VESTA REEF</h1>
      <p class="product-name">Glistening Sugar Scrub with Jojoba Beads and Lavender Mint Scent</p>
    </div>

    <div class="product-copy product-copy--facts">
      <p><strong>Ingredients:</strong> Sucrose, Carthamus tinctorius (Safflower) Seed Oil, Polysorbate 80, Tocopherol Acetate (Vitamin E), Fragrance, Silica, Phenoxyethanol</p>
      <p><strong>WARNING:</strong> This product contains natural oils that can make surfaces slippery. Use caution whenever using this product to prevent possible injury.</p>
    </div>
  </section>
</body>
</html>
```